Flyer for a marketing

We are a holistic mental health facility in need of a flyer to help promote our services and encourage more people to seek care. See the attachment to tell you more. We prefer warm green colors or rich blue. Thank you.

```html
<!DOCTYPE html>
<html lang="en">
<head>
<meta charset="utf-8">
<title>Evergreen Mind Health and Wellness – Flyer</title>
<link href="https://fonts.googleapis.com/css2?family=Fira+Sans:wght@500;600;700&family=Lato:wght@400&family=Montserrat:wght@300&display=swap" rel="stylesheet">
<style>
  :root{
    --page-bg:#e6e8eb;
    --paper:#ffffff;
    --navy:#1d2f6b;
    --brand-blue:#27a6de;
    --sky-top:#21aee6;
    --sky-bottom:#0b6cbb;
    --grey-text:#555a60;
    --lime:#8cc63f;
    --lime-light:#b6d63a;
    --green-deep:#3faa3b;
    --yellow:#f6eb3a;
    --ink:#111;
    --white:#fff;
  }
  *{box-sizing:border-box;margin:0;padding:0}
  html,body{width:1066px;height:1200px;overflow:hidden;background:var(--page-bg)}
  .flyer-frame{position:absolute;left:70px;top:0;width:926px;height:1200px;overflow:hidden}
  .flyer{position:absolute;left:0;top:0;width:892px;height:1156px;transform:scale(1.0381);transform-origin:0 0;background:var(--paper);font-family:"Lato",sans-serif}
  .backdrop{position:absolute;inset:0}
  .photo{position:absolute;left:0;top:185px;width:892px;height:455px;
    background:linear-gradient(180deg,rgba(255,255,255,1) 0%,rgba(236,238,240,.9) 10%,#e4e1de 40%,#d9cfc6 70%,#c9b8a8 100%)}
  .brand{position:absolute;left:46px;top:60px;display:flex;align-items:flex-start;gap:16px}
  .brand-dot{width:60px;height:60px;border-radius:50%;background:var(--brand-blue);margin-top:28px}
  .brand-name{font-family:"Fira Sans",sans-serif;font-weight:600;font-size:21px;line-height:25px;color:var(--navy);margin-left:60px}
  .tagline{position:absolute;left:58px;top:205px;font-family:"Montserrat",sans-serif;font-weight:300;font-size:22px;letter-spacing:1px;color:var(--navy)}
  .booking{position:absolute;left:525px;top:56px;width:343px;text-align:center}
  .booking-label{font-family:"Fira Sans",sans-serif;font-weight:500;font-size:20px;color:var(--grey-text)}
  .booking-phone{font-family:"Fira Sans",sans-serif;font-weight:600;font-size:36px;color:var(--brand-blue);line-height:44px}
  .booking-rule{height:2px;margin:4px 0 6px;background:linear-gradient(90deg,var(--lime-light),var(--brand-blue))}
  .booking-email{font-family:"Fira Sans",sans-serif;font-weight:500;font-size:18px;color:var(--grey-text)}
  .web-tab{position:absolute;left:80px;top:613px;width:400px;text-align:center;font-family:"Fira Sans",sans-serif;font-weight:700;font-size:26px;color:var(--ink)}
  .headline{position:absolute;left:49px;top:684px;color:var(--white);font-family:"Fira Sans",sans-serif;font-weight:600;text-shadow:1px 2px 3px rgba(0,0,0,.35)}
  .headline-main{font-size:42px;line-height:49px}
  .headline-sub{font-size:31px;line-height:40px;margin-top:2px}
  .divider{position:absolute;left:408px;top:695px;width:2px;height:345px;background:rgba(20,70,140,.55)}
  .info{position:absolute;left:437px;top:686px;width:430px;color:var(--white)}
  .info-lead{font-family:"Fira Sans",sans-serif;font-weight:600;font-size:24px;line-height:31px}
  .info-text{font-size:20px;line-height:26px;margin-top:16px}
  .info-heading{font-family:"Fira Sans",sans-serif;font-weight:600;font-size:20px;margin-top:30px}
  .reasons{list-style:none;margin-top:12px}
  .reasons li{position:relative;padding-left:22px;font-size:16px;line-height:18px;margin-bottom:10px}
  .reasons li::before{content:"";position:absolute;left:0;top:4px;width:12px;height:9px;border-radius:50%;background:var(--lime)}
  .slogan{position:absolute;left:49px;top:1068px;color:var(--white);font-family:"Fira Sans",sans-serif;font-weight:600;font-size:28px;line-height:32px;text-shadow:1px 2px 3px rgba(0,0,0,.35)}
  .address{position:absolute;right:46px;top:1100px;text-align:right;font-size:14px;line-height:19px;color:var(--ink)}
</style>
</head>
<body>
<div class="flyer-frame">
  <div class="flyer">
    <div class="photo" role="img" aria-label="Photo of a smiling multi-generation family standing together in a bright living room"></div>
    <svg class="backdrop" viewBox="0 0 892 1156" width="892" height="1156" aria-hidden="true">
      <defs>
        <linearGradient id="skyFill" x1="0" y1="0" x2="0" y2="1">
          <stop offset="0" stop-color="#21aee6"/>
          <stop offset="1" stop-color="#0b6cbb"/>
        </linearGradient>
        <linearGradient id="meadowFill" x1="0" y1="0" x2="1" y2="0">
          <stop offset="0" stop-color="#3faa3b"/>
          <stop offset="1" stop-color="#b6d63a"/>
        </linearGradient>
        <linearGradient id="tabFill" x1="0" y1="0" x2="1" y2="0">
          <stop offset="0" stop-color="#7cc242"/>
          <stop offset="1" stop-color="#b6d63a"/>
        </linearGradient>
      </defs>
      <rect x="0" y="640" width="892" height="516" fill="url(#skyFill)"/>
      <path d="M0 1050 C120 1028 190 1026 200 1026 C120 1030 60 1045 0 1062Z" fill="#1d4f8f"/>
      <path d="M500 1060 C650 1085 800 1070 892 1030 L892 1046 C800 1082 650 1090 500 1060Z" fill="#1d4f8f"/>
      <path d="M0 1065 C180 1025 350 1025 540 1068 C700 1102 820 1085 892 1050 L892 1156 L0 1156Z" fill="#f6eb3a"/>
      <path d="M0 1075 C180 1038 350 1040 540 1080 C700 1112 820 1098 892 1066 L892 1156 L0 1156Z" fill="url(#meadowFill)"/>
      <path d="M30 655 C32 645 38 642 48 642 L48 652Z" fill="#1d2f6b"/>
      <path d="M485 655 C483 645 477 642 467 642 L467 652Z" fill="#1d2f6b"/>
      <path d="M40 655 L62 606 L452 606 L480 655Z" fill="url(#tabFill)"/>
    </svg>

    <div class="brand">
      <div class="brand-dot" aria-hidden="true"></div>
      <div class="brand-name">Evergreen<br>Mind<br>Health<br>and<br>Wellness</div>
    </div>
    <div class="tagline">The Care You Deserve</div>

    <div class="booking">
      <div class="booking-label">Book An Appointment</div>
      <div class="booking-phone">(555) 014-2287</div>
      <div class="booking-rule"></div>
      <div class="booking-email">hello@evergreenmindhealth.com</div>
    </div>

    <div class="web-tab">evergreenmindhealth.com</div>

    <div class="headline">
      <div class="headline-main">Evergreen<br>Mind Health<br>and Wellness,</div>
      <div class="headline-sub">where deserving<br>patients meet<br>compassionate<br>providers.</div>
    </div>

    <div class="divider"></div>

    <div class="info">
      <p class="info-lead">We are accepting new patients,<br>No waiting list.</p>
      <p class="info-text">Your mental health matters, so make it a priority and call us today for an appointment.</p>
      <p class="info-heading">Why choose us?</p>
      <ul class="reasons">
        <li>We are an integrative holistic psychiatric center.</li>
        <li>Our mission is to provide compassionate quality care.</li>
        <li>We provide psychiatric services including medication management and psychotherapy.</li>
        <li>We listen, care, and empower you to live better.</li>
        <li>We accept major insurances.</li>
      </ul>
    </div>

    <div class="slogan">We Listen, Care, and Help<br>You Live A BETTER Life</div>
    <div class="address">4180 Maplewood Drive, Suite 300<br>Riverton, CA 90210. Fax (555) 017-4420</div>
  </div>
</div>
</body>
</html>
```